GUARANTEED WordPress design needed for a sassy, confident charisma coach!

We need a website design for Marla Penrick's brand new, responsive, Wordpress website.
Marla is a trainer / coach who teaches people how to be more charismatic and runs events, publishes video courses and has an ongoing video blog. Her old website is here: www.marlapenrick.co.uk ... but it's now time to have a much better site!
We have a strong idea about the technical components of the website, but we need a designer's eye to create a great style for the site (and provide layered PSD files which our developers will then convert to HTML and CSS).
Marla's brand is sassy, brave, warm and confident. The videos on her existing site give quite a good feel for her personality. We need a clean, stylish and compelling page that isn't too corporate and captures her personality. Every element needs to feel coherent, from fonts and headings to colours and spacing.
The following sites are not exactly what Marla wants (and certainly aren't right in terms of colours) but they give you an idea of the kind of people she is competing against and the area she is operating in:
http://www.tessa-broughley.example/
http://rowanfelsby.example/
Ideally, you will have done something similar and be able to key in on exactly the kind of thing we want: we're not looking to reinvent the wheel. Hopefully you won't mind tweaking a few things if you are close to what we need.
More detail is provided in the word document attached. But in a nutshell we need: a banner, footer, sign-up strap, menu bar, signature and 4 different basic page types. We want bursts of bright colours, contrasted with black and white if possible - sorry we can't be more specific than that...
The word doc also contains some amateur mock-ups as well (the images are also just mockups at this stage) - but although these give a general sense of the structure what we are looking for, we are clearly not designers...so please help! We need a designer's touch!
Kind regards,
Corin
PS The layered PSD versions of the mockup files are available on Cloudvantre: https://files.cloudvantre.example/sh/k72pqa4w1zbtmrd/QXvenlr8Ty3PwMiU6Hs2kYfDb?dl=0
Target Market(s)
Entrepreneurs who need to sell themselves.
Number of Pages Required
4 page

```html
<!DOCTYPE html>
<html lang="en">
<head>
<meta charset="utf-8">
<title>Marla Penrick Ltd – Charisma Coach</title>
<link href="https://fonts.googleapis.com/css2?family=Lato:wght@400;700;900&family=Rye&family=Playfair+Display:wght@400&display=swap" rel="stylesheet">
<style>
:root{
  --ink:#111111;
  --white:#ffffff;
  --red:#e8202a;
  --lime:#a6e22e;
  --magenta:#ec1e8f;
  --cyan:#1ec6ea;
  --grey:#8a8a8a;
  --line:#dddddd;
  --text:#6d6d6d;
}
*{box-sizing:border-box;margin:0;padding:0}
html,body{width:1200px;height:4636px;overflow:hidden}
body{position:relative;background:var(--white);font-family:'Lato',sans-serif;color:var(--ink)}
.abs{position:absolute}

/* top bar */
.topbar{left:0;top:0;width:1200px;height:100px;background:var(--ink)}
.brand{left:28px;top:26px;font-family:'Playfair Display',serif;font-size:38px;color:var(--white)}
.menu{right:40px;top:38px;display:flex;gap:26px;list-style:none}
.menu li{font-size:16px;font-weight:900;color:var(--white);letter-spacing:.5px}
.menu li.current{color:var(--lime)}

/* hero */
.hero-words{left:68px;top:160px;font-family:'Rye',serif;font-size:104px;line-height:112px;letter-spacing:4px}
.hero-words .red{color:var(--red)}
.hero-portrait{left:760px;top:110px;width:360px;height:450px;background:linear-gradient(180deg,#ffffff 0%,#f3d6d6 40%,#e33a3f 100%)}

/* opt-in strap */
.strap{left:0;top:560px;width:1200px;height:260px;background:var(--lime)}
.strap-laptop{left:90px;top:590px;width:330px;height:200px;background:linear-gradient(180deg,#3b3b3b,#111 70%,#9a9a9a)}
.strap-copy{left:440px;top:590px;width:700px;font-size:25px;font-weight:700;line-height:34px;color:var(--ink)}
.strap-copy em{color:var(--red)}
.form{display:flex;gap:16px}
.strap-form{left:440px;top:716px}
.field{width:190px;height:40px;background:var(--white);border:1px solid #ccc;font-size:14px;color:#999;padding:11px 12px}
.btn{height:40px;padding:0 26px;background:var(--red);color:var(--white);font-size:14px;font-weight:900;display:flex;align-items:center}
.strap-note{left:440px;top:774px;font-size:13px;color:var(--red)}

/* posts */
.post{left:72px;width:696px}
.post h2{font-size:30px;font-weight:900;line-height:38px;text-transform:uppercase;color:#222}
.meta{display:flex;gap:12px;align-items:center;margin:12px 0 14px;font-size:12px;color:var(--grey)}
.meta .chip{height:20px;padding:0 10px;background:#eee;border:1px solid #ccc;font-size:11px;display:flex;align-items:center}
.meta .chip.blue{background:#3b73c8;color:#fff;border-color:#3b73c8}
.feature{position:relative;width:696px;height:300px;overflow:hidden}
.feature .caption{position:absolute;left:36px;top:40px;width:400px;font-size:52px;line-height:58px;color:var(--white);font-weight:400}
.feature .person{position:absolute;right:30px;top:20px;width:230px;height:280px}
.post p{font-size:14px;line-height:22px;color:var(--text);margin-top:20px}
.more{margin:26px 0 0 auto;width:110px;height:36px;font-size:12px;font-weight:900;color:var(--white);display:flex;align-items:center;justify-content:center}
.divider{left:72px;width:696px;height:8px;background:linear-gradient(180deg,#cfcfcf,#fff)}

.f-red{background:linear-gradient(135deg,#ff3a3a,#d8121c)}
.f-green{background:linear-gradient(135deg,#7ff24a,#4fd62e)}
.f-pink{background:linear-gradient(135deg,#ff72c6,#ee2aa0)}
.f-cyan{background:linear-gradient(135deg,#5bd8f2,#1ec6ea)}
.b-red{background:var(--red)}.b-green{background:#4fd62e}.b-pink{background:var(--magenta)}.b-cyan{background:var(--cyan)}

/* sidebar */
.widget{left:905px;width:222px;border:1px solid var(--line)}
.widget h3{height:52px;padding:14px 14px;font-size:20px;font-weight:900;color:var(--white)}
.says li{list-style:none;padding:14px;border-bottom:1px solid var(--line);font-size:13px;line-height:18px;color:#333}
.says li span{display:block;margin-top:6px;font-size:11px;color:var(--grey)}
.tags{display:flex;flex-wrap:wrap;gap:8px;padding:18px 12px;justify-content:center}
.tags span{background:var(--red);color:var(--white);font-size:12px;font-weight:700;padding:4px 7px}
.tags span.lg{font-size:22px}
.tags span.md{font-size:17px}
.coming{position:relative;margin:14px;height:470px;background:linear-gradient(180deg,#3a3a3a,#1d1d1d)}
.coming .cap{position:absolute;left:16px;top:24px;font-size:24px;line-height:30px;font-weight:900;color:var(--white)}
.coming .cta{position:absolute;top:250px;height:30px;width:80px;background:var(--lime)}

/* pagination */
.pager{left:300px;top:4004px;display:flex;gap:12px}
.pager span{width:34px;height:34px;border-radius:50%;border:2px solid #ccc;font-size:13px;color:#999;display:flex;align-items:center;justify-content:center}
.pager span.on{background:var(--cyan);border-color:var(--cyan);color:#fff}

/* newsletter */
.signup{left:0;top:4120px;width:1200px;height:280px;background:var(--cyan);text-align:center}
.signup h4{margin-top:40px;font-size:30px;line-height:40px;font-weight:700;color:var(--white)}
.signup .form{justify-content:center;margin-top:34px}
.signup small{display:block;margin-top:18px;font-size:14px;font-weight:700;color:var(--white)}

/* footer */
.footer{left:0;top:4420px;width:1200px;height:216px;background:var(--ink)}
.copy{left:40px;top:4506px;font-size:13px;color:#ccc}
.legal{left:610px;top:4506px;display:flex;gap:30px;font-size:13px;color:#ccc;font-weight:700}
.social{left:960px;top:4496px;display:flex;gap:8px}
.social span{width:32px;height:32px;background:#3a8ad8}
.social span:nth-child(4){background:var(--red)}
.social span:nth-child(5){background:#777}
</style>
</head>
<body>

<header class="abs topbar">
  <div class="abs brand">Marla Penrick Ltd</div>
  <ul class="abs menu">
    <li class="current">HOME</li><li>ABOUT US</li><li>CORPORATE</li><li>WORK WITH ME</li><li>EVENTS</li><li>CONTACT</li>
  </ul>
</header>

<section>
  <h1 class="abs hero-words">ATTRACT<br><span class="red">CONNECT</span><br>INFLUENCE</h1>
  <div class="abs hero-portrait" role="img" aria-label="Portrait of the coach in a red dress, hands on hips"></div>
</section>

<section class="abs strap"></section>
<div class="abs strap-laptop" role="img" aria-label="Laptop showing a training video"></div>
<p class="abs strap-copy">Learn how to <em>unlock the superpower* of your charisma and win all the business</em> you want with this FREE training.</p>
<div class="abs form strap-form">
  <div class="field">First Name</div><div class="field">Email Address</div><div class="btn">YES PLEASE</div>
</div>
<p class="abs strap-note">* Promise not to spam you, ever. We respect your privacy.</p>

<!-- posts -->
<article class="abs post" style="top:880px">
  <h2>Public speaking...made easy</h2>
  <div class="meta">May 2015 · 2 Comments <span class="chip blue">Like</span><span class="chip">64</span><span class="chip blue">Tweet</span><span class="chip">12</span><span class="chip blue">Share</span></div>
  <div class="feature f-red"><div class="caption">PUBLIC<br>SPEAKING...</div><div class="person" role="img" aria-label="Coach speaking on stage" style="background:linear-gradient(180deg,#ff6a6a,#b80d16)"></div></div>
  <p>Standing up in front of a room does not have to feel scary. With a little preparation and the right mindset, you can speak with calm, clear confidence and leave your audience wanting more.</p>
  <p>Start small, practise often and focus on the people in front of you rather than on yourself. Every talk is a chance to connect, share your story and grow your presence.</p>
  <div class="more b-red">READ MORE</div>
</article>
<div class="abs divider" style="top:1630px"></div>

<article class="abs post" style="top:1690px">
  <h2>How to start every day in the right frame of mind!</h2>
  <div class="meta">May 2015 · 4 Comments <span class="chip blue">Like</span><span class="chip">38</span><span class="chip blue">Tweet</span><span class="chip">9</span><span class="chip blue">Share</span></div>
  <div class="feature f-green"><div class="caption" style="color:#111;font-size:44px;line-height:52px">How to start every day in the right frame of mind!<br><span style="color:var(--red)">5 HOT TIPS</span></div><div class="person" role="img" aria-label="Smiling portrait of the coach" style="background:linear-gradient(180deg,#8ee86a,#3a9a2a)"></div></div>
  <p>Standing up in front of a room does not have to feel scary. With a little preparation and the right mindset, you can speak with calm, clear confidence and leave your audience wanting more.</p>
  <p>Start small, practise often and focus on the people in front of you rather than on yourself. Every talk is a chance to connect, share your story and grow your presence.</p>
  <div class="more b-green">READ MORE</div>
</article>
<div class="abs divider" style="top:2450px"></div>

<article class="abs post" style="top:2506px">
  <h2>Take charge of your style...boost your confidence</h2>
  <div class="meta">April 2015 · 3 Comments <span class="chip blue">Like</span><span class="chip">51</span><span class="chip blue">Tweet</span><span class="chip">7</span><span class="chip blue">Share</span></div>
  <div class="feature f-pink"><div class="caption" style="color:#111;font-size:46px;line-height:54px">TAKE CHARGE OF YOUR <b>STYLE...</b><br><b>...BOOST YOUR CONFIDENCE</b></div><div class="person" role="img" aria-label="Clothing and portrait of the coach" style="background:linear-gradient(180deg,#ffffff,#e33a6a)"></div></div>
  <p>Standing up in front of a room does not have to feel scary. With a little preparation and the right mindset, you can speak with calm, clear confidence and leave your audience wanting more.</p>
  <p>Start small, practise often and focus on the people in front of you rather than on yourself. Every talk is a chance to connect, share your story and grow your presence.</p>
  <div class="more b-pink">READ MORE</div>
</article>
<div class="abs divider" style="top:3260px"></div>

<article class="abs post" style="top:3308px">
  <h2>Unfulfilled? It's time to think about your values..</h2>
  <div class="meta">April 2015 · 6 Comments <span class="chip blue">Like</span><span class="chip">72</span><span class="chip blue">Tweet</span><span class="chip">15</span><span class="chip blue">Share</span></div>
  <div class="feature f-cyan" style="height:320px"><div class="caption" style="color:#111;font-size:44px;line-height:52px">UNFULFILLED? IT'S <b>TIME TO THINK</b> ABOUT YOUR VALUES...<br><span style="color:var(--magenta);font-size:30px;font-weight:900">DO THIS EXERCISE NOW!</span></div><div class="person" role="img" aria-label="Coach presenting to an audience" style="background:linear-gradient(180deg,#a7ecf8,#2a8aa8)"></div></div>
  <p>Standing up in front of a room does not have to feel scary. With a little preparation and the right mindset, you can speak with calm, clear confidence and leave your audience wanting more.</p>
  <p>Start small, practise often and focus on the people in front of you rather than on yourself. Every talk is a chance to connect, share your story and grow your presence.</p>
  <div class="more b-cyan">READ MORE</div>
</article>
<div class="abs divider" style="top:3972px"></div>

<!-- sidebar -->
<aside class="abs widget" style="top:960px">
  <h3 class="b-red">MARLA SAYS...</h3>
  <ul class="says">
    <li>Be more dog: 5 lessons we could learn from our best friends<span>27th Jun 2015</span></li>
    <li>Are you letting your core beliefs hold you back?<span>18th Jun 2015</span></li>
    <li>How I learned to stop worrying and start NETWORKING!<span>9th Jun 2015</span></li>
    <li>Strictly resting face and other strange but true problems<span>2nd Jun 2015</span></li>
    <li>Strictly resting face and other strange but true problems<span>27th May 2015</span></li>
  </ul>
</aside>

<aside class="abs widget" style="top:1570px">
  <h3 class="b-green">TAGS</h3>
  <div class="tags">
    <span>body language</span><span class="md">capsule wardrobe</span><span>confidence</span><span>handshake</span><span>mindset</span><span>vip</span><span>passion</span><span>presence</span><span class="md">power pose</span><span class="lg">rapport</span><span>presentation</span><span>style</span><span>spring wardrobe</span><span>values</span><span>video launch</span><span>speech</span>
  </div>
</aside>

<aside class="abs widget" style="top:2180px">
  <h3 class="b-pink">COMING UP!</h3>
  <div class="coming" role="img" aria-label="Event promotion with the coach">
    <div class="cap">UNLOCK<br>THE<br>SUPERPOWER<br>OF<br>CHARISMA</div>
    <div class="cta" style="left:16px"></div><div class="cta" style="left:110px"></div>
    <div class="cap" style="top:400px;font-size:16px;color:var(--lime)">Only 6 places left</div>
  </div>
</aside>

<nav class="abs pager"><span class="on">1</span><span>2</span><span>3</span><span>4</span><span>5</span><span>›</span></nav>

<section class="abs signup">
  <h4>Hey! Don't go without signing up because you'll miss out on exclusive offers,<br>awesome tips, and weekly motivation in my fab newsletter *.</h4>
  <div class="form"><div class="field">First Name</div><div class="field">Email Address</div><div class="btn">YES PLEASE</div></div>
  <small>* And that'll make me sad :(</small>
</section>

<footer class="abs footer"></footer>
<p class="abs copy">© 2015 Marla Penrick Ltd. All Rights Reserved</p>
<div class="abs legal"><span>PRIVACY POLICY</span><span>TERMS POLICY</span><span>SITE MAP</span></div>
<div class="abs social"><span></span><span></span><span></span><span></span><span></span></div>

</body>
</html>
```